" A empresa desenvolve projetos residenciais, corporativos entre outros para público de médio/alto padrão, bem como acompanhamento/gerenciamento de obra e contam com parceiros na execução do projeto... "

```html
<!DOCTYPE html>
<html lang="pt-BR">
<head>
<meta charset="UTF-8">
<title>Bloco de Anotações — Lívia Serra</title>
<link rel="stylesheet" href="https://fonts.googleapis.com/css2?family=Montserrat:wght@400&display=swap">
<style>
  :root {
    --board: #d9d8dc;
    --paper: #ffffff;
    --ink: #2b2b2b;
    --gold: #d9b62a;
    --mist: #eeeeee;
    --label: #1e1e1e;
  }
  * { margin: 0; padding: 0; box-sizing: border-box; }
  html, body { width: 1200px; height: 1200px; overflow: hidden; }
  body {
    background: var(--board);
    font-family: "Montserrat", Arial, sans-serif;
    position: relative;
  }
  .board-label {
    position: absolute;
    left: 24px; top: 74px;
    font-size: 24px;
    color: var(--label);
    letter-spacing: 0.5px;
  }
  .notepad {
    position: absolute;
    left: 391px; top: 221px;
    width: 454px; height: 696px;
    background: var(--paper);
    box-shadow: 4px 10px 18px rgba(0,0,0,0.18);
    overflow: hidden;
  }
  .backdrop-motif {
    position: absolute;
    right: 0; top: 0;
    width: 300px; height: 300px;
    background: linear-gradient(225deg, var(--mist) 0%, rgba(238,238,238,0) 70%);
  }
  .brand {
    position: absolute;
    left: 22px; top: 130px;
    display: flex; flex-direction: column; gap: 6px;
  }
  .brand-row { display: flex; align-items: center; gap: 8px; }
  .brand-mark { width: 14px; height: 14px; background: var(--gold); }
  .brand-name { font-size: 24px; color: var(--ink); }
  .brand-tagline {
    font-size: 8px; color: var(--gold);
    letter-spacing: 1.5px; text-transform: uppercase;
    padding-left: 22px;
  }
  .signature {
    position: absolute;
    right: 30px; top: 600px;
    font-size: 24px; color: var(--ink);
  }
  .site {
    position: absolute;
    left: 17px; top: 664px;
    display: flex; align-items: center; gap: 8px;
    font-size: 10px; color: var(--ink); letter-spacing: 1.5px;
  }
  .site-bar { width: 4px; height: 12px; background: var(--gold); }
  .base-line {
    position: absolute;
    left: 0; bottom: 0;
    width: 197px; height: 4px;
    background: var(--gold);
  }
</style>
</head>
<body>
  <h1 class="board-label">BLOCO DE ANOTAÇÕES</h1>
  <section class="notepad">
    <div class="backdrop-motif" role="img" aria-label="Faint decorative brand motif in light grey"></div>
    <div class="brand">
      <div class="brand-row">
        <span class="brand-mark"></span>
        <span class="brand-name">Lívia Serra</span>
      </div>
      <span class="brand-tagline">Arquitetura e Interiores</span>
    </div>
    <p class="signature">Lívia Serra</p>
    <p class="site"><span class="site-bar"></span>www.liviaserra.com.br</p>
    <div class="base-line"></div>
  </section>
</body>
</html>
```